Criação de Layout Web-Design para Alimentos & Bebidas
A empresa queria:
" O Supermercado Vilarena está localizado em Jataí (GO), e com o intuito de divulgar suas ofertas para o publico maior de consumidores, decidiu investir no desenvolvimento de um website. "

```html
<!DOCTYPE html>
<html lang="pt-BR">
<head>
<meta charset="utf-8">
<title>Supermercado Vilarena</title>
<link href="https://fonts.googleapis.com/css2?family=Open+Sans:wght@400;600;700;800&family=Oswald:wght@500;600&display=swap" rel="stylesheet">
<style>
:root{
  --red:#c8171e;
  --yellow:#f5c400;
  --navy:#2b2e6b;
  --ink:#333;
  --muted:#777;
  --line:#dcdcdc;
  --paper:#ffffff;
  --band:#3a3a3a;
}
*{box-sizing:border-box;margin:0;padding:0}
html,body{width:1200px;height:1200px;overflow:hidden;background:var(--paper);font-family:"Open Sans",sans-serif;color:var(--ink)}
.page{position:absolute;left:330px;top:0;width:540px;height:1200px;overflow:hidden;background:var(--paper);box-shadow:0 0 6px rgba(0,0,0,.12)}
.topbar{height:34px;background:var(--yellow);display:flex;justify-content:flex-end;align-items:center;gap:14px;padding-right:18px}
.topbar .phone{font-size:13px;font-weight:700;color:var(--red);display:flex;align-items:center;gap:5px}
.topbar .login{background:var(--red);color:#fff;font-size:7px;font-weight:700;padding:4px 14px;border-radius:2px}
.nav{height:58px;background:var(--red);position:relative;display:flex;align-items:center;justify-content:space-between;padding:0 10px}
.nav ul{list-style:none;display:flex;gap:14px}
.nav a{color:#fff;font-size:11px;font-weight:800;text-decoration:none}
.brand{position:absolute;left:50%;top:-30px;transform:translateX(-50%);width:124px;height:124px;border-radius:50%;background:var(--paper);border:5px solid var(--yellow);display:flex;flex-direction:column;align-items:center;justify-content:center;z-index:2}
.brand .name{color:var(--red);font-weight:800;font-size:13px;line-height:1.1;text-align:center}
.brand .tel{color:var(--navy);font-weight:800;font-size:12px;margin-top:4px}
.hero{height:305px;position:relative;background:linear-gradient(100deg,#6c8a3a 0%,#a6803a 30%,#e6e0d2 60%,#f3efe8 100%)}
.hero .headline{position:absolute;left:22px;top:170px;font-family:"Oswald",sans-serif;font-size:25px;line-height:1.15;color:var(--paper)}
.hero .headline span{display:inline-block;background:rgba(232,180,20,.92);padding:2px 10px;margin-bottom:3px}
.offers{padding:14px 64px 0;height:305px;position:relative}
.sec-title{font-weight:800;font-size:17px;color:var(--navy);border-bottom:3px solid var(--red);display:inline-block;padding-bottom:2px}
.tabs{display:flex;gap:3px;margin-top:10px;border-bottom:2px solid var(--red)}
.tabs span{flex:1;text-align:center;font-size:6px;font-weight:700;background:#e8e8e8;color:var(--muted);padding:5px 0}
.tabs .on{background:var(--paper);color:var(--red);border:1px solid var(--line);border-bottom:none}
.grid{display:grid;grid-template-columns:repeat(4,1fr);gap:12px 10px;margin-top:14px}
.card{position:relative}
.card .pic{height:52px;background:var(--paper);border:1px solid #eee;display:flex;align-items:center;justify-content:center}
.card .pack{width:30px;height:40px;border-radius:3px}
.card .tag{position:absolute;right:0;top:0;width:0;height:0;border-top:26px solid var(--red);border-left:26px solid transparent}
.card .bar{background:var(--navy);color:#fff;display:flex;justify-content:space-between;align-items:center;padding:3px 4px;font-size:7px;font-weight:700}
.card .bar b{font-size:9px}
.card .desc{font-size:6px;color:var(--muted);margin-top:3px}
.arrow{position:absolute;font-size:16px;color:var(--navy);font-weight:700}
.search{padding:0 64px;height:72px}
.search h3{font-size:15px;font-weight:600;color:var(--navy)}
.search h3 b{color:var(--red)}
.search .row{display:flex;gap:6px;margin-top:10px}
.search .sel{width:88px;border:1px solid var(--line);font-size:7px;color:var(--muted);padding:5px 6px;display:flex;justify-content:space-between}
.btn{background:var(--red);color:#fff;font-size:7px;font-weight:700;padding:5px 12px;display:inline-block;border-radius:2px}
.cols{display:grid;grid-template-columns:repeat(3,1fr);gap:12px;padding:0 64px;height:196px}
.cols h4{font-size:14px;font-weight:800;color:var(--navy);line-height:1.05;height:36px;display:flex;align-items:flex-end;border-bottom:2px solid var(--red);padding-bottom:3px}
.cols .ph{height:70px;margin-top:8px}
.cols p{font-size:6px;color:var(--muted);line-height:1.4;margin:6px 0}
.news{height:76px;background:var(--band);display:flex;align-items:center;justify-content:space-between;padding:0 60px 0 80px;margin-top:8px}
.news .msg{color:#fff;font-size:12px;line-height:1.3;text-align:center}
.news .msg b{color:var(--yellow)}
.news .msg small{font-size:9px;display:block}
.news form{display:flex;flex-direction:column;gap:4px;width:170px}
.news .in{background:#fff;font-size:7px;color:var(--muted);padding:4px 6px}
.footer{height:142px;background:var(--red);display:flex;align-items:center;justify-content:center}
.footer .fbrand{display:flex;flex-direction:column;align-items:center;background:var(--paper);border-radius:50%;width:110px;height:110px;justify-content:center;border:4px solid var(--yellow)}
.footer .name{color:var(--red);font-weight:800;font-size:12px;text-align:center;line-height:1.1}
.footer .tel{color:var(--navy);font-weight:800;font-size:11px;margin-top:4px}
</style>
</head>
<body>
<div class="page">
  <header>
    <div class="topbar">
      <span class="phone"><svg width="11" height="11" viewBox="0 0 24 24"><path fill="#c8171e" d="M6.6 10.8a15 15 0 0 0 6.6 6.6l2.2-2.2c.3-.3.7-.4 1-.2 1.1.4 2.3.6 3.6.6.6 0 1 .4 1 1V20c0 .6-.4 1-1 1A17 17 0 0 1 3 4c0-.6.4-1 1-1h3.5c.6 0 1 .4 1 1 0 1.3.2 2.5.6 3.6.1.3 0 .7-.2 1z"/></svg>(64) 3555 0142</span>
      <span class="login">LOGIN</span>
    </div>
    <nav class="nav">
      <ul><li><a href="#">INICIO</a></li><li><a href="#">INSTITUCIONAL</a></li></ul>
      <div class="brand"><span class="name">Supermercado<br>Vilarena</span><span class="tel">3555-0199</span></div>
      <ul><li><a href="#">OFERTAS</a></li><li><a href="#">RECEITAS</a></li><li><a href="#">CONTATO</a></li></ul>
    </nav>
  </header>

  <section class="hero" role="img" aria-label="Foto de mulher sorridente segurando cesta de compras na seção de hortifrúti">
    <div class="headline"><span>AGORA TEMOS UM SITE</span><br><span>EXCLUSIVO PARA VOCÊ</span></div>
  </section>

  <section class="offers">
    <h2 class="sec-title">Ofertas</h2>
    <div class="tabs"><span class="on">MERCEARIA</span><span>LATICÍNIOS</span><span>BEBIDAS</span><span>ATACADO</span><span>RECEITAS EM DESTAQUE</span></div>
    <span class="arrow" style="left:40px;top:112px">‹</span>
    <span class="arrow" style="right:40px;top:112px">›</span>
    <span class="arrow" style="left:40px;top:200px">‹</span>
    <span class="arrow" style="right:40px;top:200px">›</span>
    <div class="grid">
      <div class="card"><div class="pic"><div class="pack" role="img" aria-label="Embalagem de açúcar" style="background:#e8d7d7"></div></div><div class="bar"><b>R$ 1,99</b><span>COMPRAR</span></div><p class="desc">Açúcar Refinado - Pacote 1kg</p></div>
      <div class="card"><div class="pic"><div class="pack" role="img" aria-label="Caixa de leite" style="background:#e6a8a8"></div></div><div class="tag"></div><div class="bar"><b>R$ 1,99</b><span>COMPRAR</span></div><p class="desc">Leite UHT Integral - Caixa 1L</p></div>
      <div class="card"><div class="pic"><div class="pack" role="img" aria-label="Pacote de farinha" style="background:#c8cfe0"></div></div><div class="tag"></div><div class="bar"><b>R$ 1,99</b><span>COMPRAR</span></div><p class="desc">Farinha de Trigo - Pacote 1kg</p></div>
      <div class="card"><div class="pic"><div class="pack" role="img" aria-label="Pacote de arroz" style="background:#b9c6de"></div></div><div class="bar"><b>R$ 1,99</b><span>COMPRAR</span></div><p class="desc">Arroz Tipo 1 - Pacote 5kg</p></div>
      <div class="card"><div class="pic"><div class="pack" role="img" aria-label="Embalagem de açúcar" style="background:#e8d7d7"></div></div><div class="bar"><b>R$ 1,99</b><span>COMPRAR</span></div><p class="desc">Açúcar Refinado - Pacote 1kg</p></div>
      <div class="card"><div class="pic"><div class="pack" role="img" aria-label="Caixa de leite" style="background:#e6a8a8"></div></div><div class="tag"></div><div class="bar"><b>R$ 1,99</b><span>COMPRAR</span></div><p class="desc">Leite UHT Integral - Caixa 1L</p></div>
      <div class="card"><div class="pic"><div class="pack" role="img" aria-label="Pacote de farinha" style="background:#c8cfe0"></div></div><div class="tag"></div><div class="bar"><b>R$ 1,99</b><span>COMPRAR</span></div><p class="desc">Farinha de Trigo - Pacote 1kg</p></div>
      <div class="card"><div class="pic"><div class="pack" role="img" aria-label="Pacote de arroz" style="background:#b9c6de"></div></div><div class="bar"><b>R$ 1,99</b><span>COMPRAR</span></div><p class="desc">Arroz Tipo 1 - Pacote 5kg</p></div>
    </div>
  </section>

  <section class="search">
    <h3>Não encontrou <b>o que está procurando</b>?</h3>
    <div class="row">
      <span class="sel">Categoria <span>▾</span></span>
      <span class="sel">Produto <span>▾</span></span>
      <span class="btn">PESQUISAR</span>
    </div>
  </section>

  <section class="cols">
    <article>
      <h4>Receitas</h4>
      <div class="ph" role="img" aria-label="Foto de prato de peixe com legumes" style="background:linear-gradient(135deg,#e9e2c8,#c9a95a)"></div>
      <p>Confira receitas práticas e saborosas preparadas com os produtos das nossas ofertas da semana para toda a família.</p>
      <span class="btn">VER RECEITAS</span>
    </article>
    <article>
      <h4>Cartões de Alimentação</h4>
      <div class="ph" role="img" aria-label="Foto de equipe em reunião de escritório" style="background:linear-gradient(135deg,#d8d6d2,#8d8b88)"></div>
      <p>Aceitamos os principais cartões de alimentação e refeição. Facilite as compras da sua empresa e dos colaboradores.</p>
      <span class="btn">SAIBA MAIS</span>
    </article>
    <article>
      <h4>Trabalhe Conosco</h4>
      <div class="ph" role="img" aria-label="Foto de profissional em ambiente de trabalho" style="background:linear-gradient(135deg,#ececec,#6f6f6f)"></div>
      <p>Faça parte da nossa equipe. Envie seu currículo e venha crescer junto com o supermercado que mais cresce na região.</p>
      <span class="btn">SAIBA MAIS</span>
    </article>
  </section>

  <section class="news">
    <div class="msg">Receba nossas <b>ofertas</b>!<small>Seja o 1º a saber de todas<br>nossas ofertas. <b>CADASTRE-SE</b></small></div>
    <form>
      <span class="in">Nome</span>
      <span class="in">E-mail</span>
      <span class="btn" style="align-self:flex-start">CADASTRE-SE</span>
    </form>
  </section>

  <footer class="footer">
    <div class="fbrand"><span class="name">Supermercado<br>Vilarena</span><span class="tel">3555-0199</span></div>
  </footer>
</div>
</body>
</html>
```